Business Card Design

We need a new business card design for our company, Lumen Forge.

Our website: www.brightrow7.ca

We are open to all ideas, from professional to very creative.
Updates

Design update requests:

1. We would like to see some examples with "BrightRow7" instead of "Lumen Forge" as the company name.
2. Would like to see "Software | Web | Branding" included on the card somewhere as well.

Thanks.

We are really trying to express the nature of our business through our business card.  "Lumen" can be misconstrued for the health industry, so use of "BrightRow7" and the "Software | Web | Branding" slogan are key to understanding our business.

We have uploaded a new PSD which includes a monitor, tablet, and phone screen.  This represents the flexibility of web applications and is another tool we would like to see used on business cards.

We will be eliminating designs today and will await updated designs with these new specs.

Thank-you.

Industry/Entity Type

Business

Requirements
Must have
• Content:
First M. Last
Managing Partner
e. email@brightrow7.ca
p. 555.555.5555

```html
<!DOCTYPE html>
<html lang="en">
<head>
<meta charset="utf-8">
<title>Lumen Forge – Business Card</title>
<link href="https://fonts.googleapis.com/css2?family=Arimo:wght@400;700&display=swap" rel="stylesheet">
<style>
  :root {
    --card-bg: #ffffff;
    --name-blue: #1d6a86;
    --accent-blue: #1b98d5;
    --tagline-blue: #1f6d8e;
    --brand-grey: #5a5f63;
    --icon-blue: #2a6f93;
    --band-slate: #3f5666;
    --band-blue: #1f8fd0;
    --band-ink: #1c2228;
    --band-sky: #8fd0f0;
    --band-steel: #6c8594;
    --deco-light: #d6eef9;
  }
  * { margin: 0; padding: 0; box-sizing: border-box; }
  html, body {
    width: 1200px; height: 686px; overflow: hidden;
    background: var(--card-bg);
    font-family: "Arimo", Arial, sans-serif;
  }
  .card { position: relative; width: 1200px; height: 686px; background: var(--card-bg); }

  .brand {
    position: absolute; right: 43px; top: 70px;
    display: flex; align-items: center; gap: 22px;
  }
  .brand-mark { width: 58px; height: 58px; background: var(--accent-blue); }
  .brand-name {
    font-weight: 700; font-size: 62px; letter-spacing: 2px;
    color: var(--brand-grey); line-height: 1;
  }
  .tagline {
    position: absolute; right: 43px; top: 194px;
    font-weight: 700; font-size: 27px; letter-spacing: 0.5px;
    color: var(--tagline-blue);
  }

  .person { position: absolute; left: 103px; top: 258px; }
  .person-name { font-weight: 700; font-size: 46px; color: var(--name-blue); line-height: 1.1; }
  .person-role { margin-top: 14px; font-size: 33px; color: var(--accent-blue); }

  .deco-squares {
    position: absolute; left: 0; top: 410px; width: 250px; height: 245px;
    background: radial-gradient(ellipse at 30% 70%, var(--deco-light) 0%, rgba(214,238,249,0.4) 45%, rgba(255,255,255,0) 75%);
  }

  .contacts {
    position: absolute; left: 748px; top: 440px; list-style: none;
  }
  .contacts li {
    display: flex; align-items: center; height: 73px;
    font-size: 31px; color: var(--accent-blue);
  }
  .contacts svg { width: 40px; height: 40px; margin-right: 32px; flex: none; }

  .band { position: absolute; left: 0; bottom: 0; width: 100%; height: 10px; display: flex; }
  .band span { flex: 1; }
  .band .s1 { background: var(--band-slate); }
  .band .s2 { background: var(--band-blue); }
  .band .s3 { background: var(--band-ink); }
  .band .s4 { background: var(--band-sky); }
  .band .s5 { background: var(--band-steel); }
</style>
</head>
<body>
<div class="card">
  <div class="brand">
    <span class="brand-mark"></span>
    <span class="brand-name">LUMEN FORGE</span>
  </div>
  <div class="tagline">SOFTWARE | WEB | BRANDING</div>

  <div class="person">
    <div class="person-name">First M. Last</div>
    <div class="person-role">Managing Partner</div>
  </div>

  <div class="deco-squares" role="img" aria-label="Soft light-blue decorative square pattern"></div>

  <ul class="contacts">
    <li>
      <svg viewBox="0 0 40 40" aria-hidden="true">
        <circle cx="20" cy="20" r="16" fill="none" stroke="var(--icon-blue)" stroke-width="3"/>
        <ellipse cx="20" cy="20" rx="7" ry="16" fill="none" stroke="var(--icon-blue)" stroke-width="2.5"/>
        <line x1="4" y1="20" x2="36" y2="20" stroke="var(--icon-blue)" stroke-width="2.5"/>
      </svg>
      www.brightrow7.ca
    </li>
    <li>
      <svg viewBox="0 0 40 40" aria-hidden="true">
        <rect x="4" y="9" width="32" height="22" fill="none" stroke="var(--icon-blue)" stroke-width="2.5"/>
        <polyline points="4,9 20,22 36,9" fill="none" stroke="var(--icon-blue)" stroke-width="2.5"/>
      </svg>
      email@brightrow7.ca
    </li>
    <li>
      <svg viewBox="0 0 40 40" aria-hidden="true">
        <path d="M11 5 L17 11 L13 16 C15 21 19 25 24 27 L29 23 L35 29 L30 35 C18 34 6 22 5 10 Z" fill="var(--icon-blue)"/>
      </svg>
      555.555.5555
    </li>
  </ul>

  <div class="band">
    <span class="s1"></span><span class="s2"></span><span class="s3"></span><span class="s4"></span><span class="s5"></span>
  </div>
</div>
</body>
</html>
```